Technology management company looking for a new website with a professional look

Brennick IT is a recently re-branded technology management company that is looking for a website design to match its personalized approach and friendly culture.

We would like to see a specialized, but related, page style for each of our main service offerings of:

• Commercial IT Support (This is our primary focus)
• Commercial Phone Systems (We partner with http://www.voxtrell.com/ for our phone systems)
• Point of Sale Systems (We partner with http://www.tillmora.com/ for our POS systems.
• Web Design
• Hollow Pine Computers (Our residential computer service offering, branded as Hollow Pine Computers)

The Hollow Pine Computers page should be build upon the Hollow Pine Computers logo, the other four pages should be branded as Brennick IT.

These five separate pages should have subtle, yet clearly defined links to one another. They should also each have a Home, Products, Service, and Company in the menu.

The website should have a clean design with professional appeal, but not appear too sterile or uninviting. It needs to have a simple, easy to navigate menu interface along the top. We would also like the site to be mobile friendly.

It should also allow us to easily tie in links to our social media pages (Facebook, LinkedIn, Twitter and Google+) and provide easy access to our contact information from each page.

This is a link to our old website www.hollowpinecomputers.com

We don't currently have copy available. The text and menu design should be easily editable and expandable so we can use the design to fit our copy.

In general we are looking for a concept we can modify to fit our needs.

We need this design to be available with layers in a .psd format.

Target Market(s)

Small to mid-size businesses.

Industry/Entity Type

Information Technology

Number of Pages Required

5+ page

Font styles to use
Sans Serif

Requirements
Must have
• Mobile Friendly
• Professional Type Face
• Unity between all pages
• .PSD Format
Nice to have
• Themed with our logo
Should not have
• Bubbly unprofessional typeface. No comic sans.

```html
<!DOCTYPE html>
<html lang="en">
<head>
<meta charset="utf-8">
<title>Brennick IT</title>
<link href="https://fonts.googleapis.com/css2?family=Lato:wght@400;700;900&family=Open+Sans:wght@400;600;700&display=swap" rel="stylesheet">
<style>
:root{
  --orange:#f26a21;
  --orange-dark:#d9560f;
  --navy:#1d4f86;
  --blue:#23589a;
  --ink:#333;
  --muted:#777;
  --light:#f2f2f2;
  --footer:#4a4a4a;
  --footer-dark:#3b3b3b;
}
*{box-sizing:border-box;margin:0;padding:0}
html,body{width:692px;height:1200px;overflow:hidden;background:#fff}
body{font-family:"Open Sans",Arial,sans-serif;color:var(--ink);position:relative}
.abs{position:absolute}
/* header */
.site-header{left:0;top:0;width:692px;height:40px;background:#fff;border-bottom:1px solid #e5e5e5}
.brand{left:18px;top:8px;display:flex;align-items:center;gap:6px;font-family:"Lato",sans-serif;font-weight:900;font-size:20px;color:var(--navy)}
.brand-mark{width:20px;height:20px;border-radius:50%;background:var(--orange)}
.contact-strip{right:18px;top:3px;font-size:7px;color:var(--muted);display:flex;gap:14px}
.main-nav{right:18px;top:17px;display:flex;font-size:7.5px;font-weight:600;text-transform:uppercase}
.main-nav a{padding:5px 9px;color:#555;text-decoration:none;border-right:1px solid #ddd}
.main-nav a:last-child{border-right:none}
.main-nav a.active{background:var(--orange);color:#fff}
/* hero */
.hero{left:0;top:40px;width:692px;height:283px;background:radial-gradient(ellipse at 45% 40%,#f7b15a 0%,#c9651c 35%,#5a2a10 70%,#1f1209 100%)}
.hero-caption{right:26px;top:246px;font-family:"Lato",sans-serif;font-weight:700;color:#fff;font-size:17px;line-height:21px;text-transform:uppercase;text-align:left;background:rgba(0,0,0,.35);padding:4px 8px}
.hero-dots{left:22px;top:300px;display:flex;gap:6px}
.hero-dots span{width:7px;height:7px;border-radius:50%;background:#fff;opacity:.6}
.hero-dots span:first-child{opacity:1}
/* welcome */
.welcome{left:0;top:323px;width:692px;height:220px;background:var(--light)}
.section-title{font-family:"Lato",sans-serif;font-weight:700;font-size:19px;text-align:center;width:692px;left:0;color:#333;text-transform:uppercase;letter-spacing:.5px}
.section-title em{font-style:normal;color:var(--orange)}
.title-rule{left:306px;width:80px;height:2px;background:var(--orange)}
.welcome-text{left:46px;top:384px;width:340px;font-size:7px;line-height:11px;color:#666}
.btn{background:var(--orange);color:#fff;font-weight:700;text-transform:uppercase;display:flex;align-items:center;justify-content:center}
.read-more{left:46px;top:497px;width:64px;height:16px;font-size:7px}
.video{left:412px;top:392px;width:234px;height:108px;background:linear-gradient(135deg,#8fa9bf,#4d6782 60%,#2c3c4f)}
.play{left:510px;top:426px;width:40px;height:40px}
/* services */
.service{width:108px;text-align:center}
.service-icon{width:44px;height:44px;margin:0 auto;display:block}
.service h3{font-size:8.5px;font-weight:600;color:var(--blue);margin-top:8px;line-height:11px;height:22px;display:flex;align-items:flex-end;justify-content:center}
.service p{font-size:6.5px;line-height:9px;color:#666;margin-top:4px}
/* banner */
.cta-band{left:0;top:785px;width:692px;height:103px;background:linear-gradient(90deg,#1b4c86,#2662a6)}
.cta-text{left:40px;top:803px;width:420px;font-family:"Lato",sans-serif;font-weight:900;font-size:20px;line-height:26px;color:#fff}
.cta-btn{left:490px;top:815px;width:150px;height:40px;font-family:"Lato",sans-serif;font-size:18px;font-weight:900;border-radius:2px}
/* lower */
.sub-title{font-family:"Lato",sans-serif;font-weight:900;font-size:12px;text-transform:uppercase;color:#333}
.sub-title small{font-size:7px;color:var(--orange);font-weight:700;margin-left:4px}
.sub-title em{font-style:normal;color:var(--orange)}
.partner{height:26px;display:flex;align-items:center;gap:4px;font-family:"Open Sans",sans-serif;font-weight:700;font-size:11px;color:var(--navy)}
.partner i{width:10px;height:10px;background:var(--orange);display:block}
.live-chat{left:40px;top:994px;font-family:"Lato",sans-serif;font-weight:700;font-size:12px}
.avatar{left:370px;top:944px;width:56px;height:56px;border-radius:50%;background:linear-gradient(#b8b2aa,#7d7570)}
.quote{left:440px;top:944px;width:220px;font-size:7px;line-height:10.5px;color:#666}
.quote-name{left:372px;top:1006px;font-size:7px;color:#444}
/* footer */
.site-footer{left:0;top:1050px;width:692px;height:128px;background:var(--footer)}
.footer-nav{left:20px;top:1060px;display:flex;font-size:7px;color:#ddd;gap:0}
.footer-nav span{padding:0 7px;border-right:1px solid #777}
.footer-nav span:first-child{padding-left:0}
.footer-nav span:last-child{border:none}
.footer-rule{left:20px;top:1077px;width:652px;height:1px;background:#666}
.footer-col{font-size:7px;line-height:11px;color:#ccc}
.footer-col strong{color:#fff}
.email-box{left:458px;top:1090px;width:112px;height:16px;background:#fff;font-size:6.5px;color:#999;padding:4px 6px}
.submit{left:458px;top:1112px;width:112px;height:16px;font-size:7.5px}
.footer-deco{left:592px;top:1088px;width:72px;height:72px}
.bottom-bar{left:0;top:1178px;width:692px;height:22px;background:var(--orange)}
.copyright{left:20px;top:1184px;font-size:7px;color:#fff}
.social{right:18px;top:1182px;display:flex;gap:5px}
.social span{width:14px;height:14px;border-radius:50%;background:#fff;opacity:.9}
</style>
</head>
<body>

<header class="site-header abs">
  <div class="brand abs"><span class="brand-mark"></span>Brennick IT</div>
  <div class="contact-strip abs"><span>✉ support@brennickit.co.uk</span><span>☎ 513-482-7061</span></div>
  <nav class="main-nav abs"><a class="active">Home</a><a>Products ▾</a><a>Service ▾</a><a>Company Overview</a><a>Contact</a></nav>
</header>

<section class="hero abs" role="img" aria-label="Businessman touching a glowing network of connected people icons"></section>
<div class="hero-caption abs">Professional Service<br>Customized to meet your needs</div>
<div class="hero-dots abs"><span></span><span></span><span></span></div>

<section class="welcome abs"></section>
<h2 class="section-title abs" style="top:340px">Welcome to <em>Brennick IT</em></h2>
<div class="title-rule abs" style="top:366px"></div>
<p class="welcome-text abs">Lorem ipsum dolor sit amet, consectetuer adipiscing elit, sed diam nonummy nibh euismod tincidunt ut laoreet dolore magna aliquam erat volutpat. Ut wisi enim ad minim veniam, quis nostrud exerci tation ullamcorper suscipit lobortis nisl ut aliquip ex ea commodo consequat. Duis autem vel eum iriure dolor in hendrerit in vulputate velit esse molestie consequat, vel illum dolore eu feugiat nulla facilisis at vero eros et accumsan et iusto odio dignissim qui blandit praesent luptatum zzril delenit augue duis dolore te feugait nulla facilisi. Lorem ipsum dolor sit amet, consectetuer adipiscing elit, sed diam nonummy nibh euismod tincidunt ut laoreet dolore magna aliquam erat volutpat. Ut wisi enim ad minim veniam, quis nostrud exerci tation ullamcorper suscipit lobortis nisl ut aliquip ex ea commodo consequat.</p>
<div class="read-more btn abs">Read More</div>
<div class="video abs" role="img" aria-label="Video still of a team meeting around a whiteboard"></div>
<svg class="play abs" viewBox="0 0 40 40"><circle cx="20" cy="20" r="18" fill="rgba(0,0,0,.35)" stroke="#fff" stroke-width="2"/><path d="M16 12l12 8-12 8z" fill="#fff"/></svg>

<h2 class="section-title abs" style="top:566px">Our <em>Services</em></h2>
<div class="title-rule abs" style="top:592px"></div>

<div class="service abs" style="left:46px;top:620px">
  <svg class="service-icon" viewBox="0 0 44 44"><circle cx="22" cy="22" r="21" fill="var(--blue)"/><circle cx="22" cy="22" r="17" fill="none" stroke="#fff" stroke-width="1"/><path d="M16 28l10-10m-2-3l5 5-3 3-5-5zM14 30l3-1-2-2z" stroke="#fff" stroke-width="2" fill="none"/></svg>
  <h3>Commercial IT<br>Support</h3><p>Lorem ipsum dolor sit amet consectetuer adipiscing elit sed diam nonummy</p>
</div>
<div class="service abs" style="left:166px;top:620px">
  <svg class="service-icon" viewBox="0 0 44 44"><circle cx="22" cy="22" r="21" fill="var(--blue)"/><circle cx="22" cy="22" r="17" fill="none" stroke="#fff" stroke-width="1"/><path d="M15 15c0 8 6 14 14 14l2-4-4-2-2 2c-3-1-5-3-6-6l2-2-2-4z" fill="#fff"/></svg>
  <h3>Commercial Phone<br>Systems</h3><p>Lorem ipsum dolor sit amet consectetuer adipiscing elit sed diam nonummy</p>
</div>
<div class="service abs" style="left:292px;top:620px">
  <svg class="service-icon" viewBox="0 0 44 44"><circle cx="22" cy="22" r="21" fill="var(--blue)"/><circle cx="22" cy="22" r="17" fill="none" stroke="#fff" stroke-width="1"/><rect x="17" y="13" width="12" height="18" rx="2" fill="none" stroke="#fff" stroke-width="2" transform="rotate(30 22 22)"/></svg>
  <h3>Point of Sale<br>Systems</h3><p>Lorem ipsum dolor sit amet consectetuer adipiscing elit sed diam nonummy</p>
</div>
<div class="service abs" style="left:418px;top:620px">
  <svg class="service-icon" viewBox="0 0 44 44"><circle cx="22" cy="22" r="21" fill="var(--blue)"/><circle cx="22" cy="22" r="17" fill="none" stroke="#fff" stroke-width="1"/><rect x="13" y="14" width="18" height="12" fill="none" stroke="#fff" stroke-width="2"/><path d="M19 30h6M22 26v4" stroke="#fff" stroke-width="2"/></svg>
  <h3>Web<br>Design</h3><p>Lorem ipsum dolor sit amet consectetuer adipiscing elit sed diam nonummy</p>
</div>
<div class="service abs" style="left:540px;top:620px">
  <svg class="service-icon" viewBox="0 0 44 44"><circle cx="22" cy="22" r="21" fill="var(--blue)"/><circle cx="22" cy="22" r="17" fill="none" stroke="#fff" stroke-width="1"/><rect x="12" y="14" width="14" height="10" fill="none" stroke="#fff" stroke-width="2"/><rect x="28" y="13" width="5" height="16" fill="none" stroke="#fff" stroke-width="2"/><path d="M15 29h8" stroke="#fff" stroke-width="2"/></svg>
  <h3>Hollow Pine<br>Computers</h3><p>Lorem ipsum dolor sit amet consectetuer adipiscing elit sed diam nonummy</p>
</div>

<section class="cta-band abs"></section>
<p class="cta-text abs">Lorem ipsum dolor sit amet consectetuer adipiscing elit sed diam nonummy ipsum.</p>
<div class="cta-btn btn abs">Call us today!</div>

<h3 class="sub-title abs" style="left:40px;top:906px">Solutions<small>for your tech needs</small></h3>
<div class="partner abs" style="left:40px;top:936px"><i></i>Voxtrell</div>
<div class="partner abs" style="left:128px;top:936px"><i></i>Tillmora</div>
<div class="partner abs" style="left:214px;top:936px"><i></i>RemoteLink</div>
<p class="live-chat abs">Live chat weekdays from 8am to 6pm.</p>

<h3 class="sub-title abs" style="left:370px;top:906px">What our <em>customer say</em></h3>
<div class="avatar abs" role="img" aria-label="Customer portrait"></div>
<p class="quote abs">“Lorem ipsum dolor sit amet consectetuer adipiscing elit sed diam nonummy nibh euismod tincidunt ut laoreet dolore magna aliquam erat volutpat. Ut wisi enim ad minim veniam quis nostrud exerci tation ullamcorper suscipit lobortis nisl ut aliquip ex ea commodo.”</p>
<p class="quote-name abs">– Mara Tellis</p>

<footer class="site-footer abs"></footer>
<div class="footer-nav abs"><span>Home</span><span>Products</span><span>Service</span><span>Company Overview</span><span>Contact Us</span></div>
<div class="footer-rule abs"></div>
<div class="footer-col abs" style="left:20px;top:1090px"><strong>BRENNICK IT</strong><br>Unit 4 Harlow Yard<br>Westfield, WX2 7TN<br>Registered no. 204187</div>
<div class="footer-col abs" style="left:250px;top:1090px">☎ (513) 482-7061<br>☎ (513) 482-7062<br>✉ info@brennickit.com<br>⌂ www.brennickit.com</div>
<div class="email-box abs">Enter Your Email Here</div>
<div class="submit btn abs">Submit</div>
<svg class="footer-deco abs" viewBox="0 0 72 72"><circle cx="36" cy="36" r="30" fill="none" stroke="#5e5e5e" stroke-width="6"/></svg>
<div class="bottom-bar abs"></div>
<p class="copyright abs">© 2015 Brennick IT. All Rights Reserved.</p>
<div class="social abs"><span></span><span></span><span></span><span></span></div>

</body>
</html>
```